"Oral Surgery Office needs a Business Card Design with Logo"

We need a logo design and business card. The name of the office is Tassingford Oral Surgery & Implant Center. The final design should communicate uniqueness as well as highly class office. The business card should emphasize power. I included the current business card below. Please design something unique

Target Market(s)

Dentists & Patients

Industry/Entity Type

Dental

Contact Information for Business Card

Unique Design to show success, prestige, Style, unmatched performance

Font styles to use
Serif

Colors
1b1b1b
ffffff
0556a4

Requirements
Must have
• Bussiness Name, Doctor's Name, Website, phone and Fax, email, office address
• Color should be either Black and White or Blue and White
Nice to have
• Clean look
Should not have
• the business card shouldn't be too busy. I feel like the old business card was too busy

```html
<!DOCTYPE html>
<html lang="en">
<head>
<meta charset="utf-8">
<title>Tassingford Oral Surgery &amp; Implant Center — Business Card</title>
<link rel="stylesheet" href="https://fonts.googleapis.com/css2?family=Open+Sans:wdth,wght@75..100,400..700&display=swap">
<style>
  :root {
    --ink: #1b1b1b;
    --paper: #ffffff;
    --brand-blue: #2aa3dc;
    --backdrop: #e9e9e9;
  }
  * { box-sizing: border-box; margin: 0; padding: 0; }
  html, body {
    width: 1200px; height: 1000px; overflow: hidden;
    background: var(--backdrop);
    font-family: "Open Sans", Arial, sans-serif;
    color: var(--ink);
  }
  .card-frame {
    position: absolute; left: 100px; top: 201px;
    width: 999px; height: 597px;
    box-shadow: 0 6px 24px rgba(0,0,0,.18);
  }
  .card {
    position: absolute; left: 0; top: 0;
    width: 666px; height: 398px;
    background: var(--paper);
    transform: scale(1.5); transform-origin: 0 0;
    overflow: hidden;
  }
  .brand-mark {
    position: absolute; left: 32px; top: 31px;
    width: 104px; height: 104px;
    background: var(--ink);
  }
  .brand-name {
    position: absolute; left: 150px; top: 52px;
    font-weight: 700; font-stretch: 75%;
    color: var(--ink);
    line-height: 1;
  }
  .brand-name__line1 { display: block; font-size: 30px; letter-spacing: .2px; }
  .brand-name__line2 { display: block; margin-top: 13px; font-size: 16px; letter-spacing: 7.4px; }
  .brand-rule {
    position: absolute; left: 150px; top: 88px;
    width: 276px; height: 1.5px; background: var(--brand-blue);
  }
  .doctor {
    position: absolute; right: 32px; top: 195px;
    text-align: right;
  }
  .doctor__name { font-size: 21px; font-weight: 600; line-height: 28px; }
  .doctor__name .credential { font-weight: 400; }
  .doctor__specialty { font-size: 16px; color: var(--brand-blue); line-height: 24px; }
  .contact-list {
    position: absolute; left: 32px; top: 220px;
    list-style: none; font-size: 16px; line-height: 23.5px;
  }
  .contact-list li { display: flex; align-items: center; gap: 8px; }
  .contact-list svg { width: 16px; height: 14px; fill: var(--ink); flex: none; }
  .address {
    position: absolute; left: 32px; top: 320px;
    font-size: 16px; line-height: 24px;
  }
  .card-bands { position: absolute; left: 0; bottom: 0; width: 666px; height: 32px; }
</style>
</head>
<body>
  <div class="card-frame">
    <div class="card">
      <div class="brand-mark" aria-hidden="true"></div>
      <div class="brand-name">
        <span class="brand-name__line1">TASSINGFORD ORAL SURGERY</span>
        <span class="brand-name__line2">&amp; IMPLANT CENTER</span>
      </div>
      <div class="brand-rule"></div>

      <div class="doctor">
        <p class="doctor__name">Dr. Miriam Holloway<span class="credential">, D.D.S</span></p>
        <p class="doctor__specialty">Oral &amp; Maxillofacial Surgery</p>
      </div>

      <ul class="contact-list">
        <li>
          <svg viewBox="0 0 16 14" aria-hidden="true"><path d="M1 4c0-2 3-3 7-3s7 1 7 3v1.5h-3.5V4h-7v1.5H1zM4 7l1.5-2h5L12 7v6H4zm4 1.2a1.6 1.6 0 1 0 0 3.2 1.6 1.6 0 0 0 0-3.2z"/></svg>
          <span>555 - 210 - 4700</span>
        </li>
        <li>
          <svg viewBox="0 0 16 14" aria-hidden="true"><path d="M4 0h8v4H4zM1 5h14v6h-3V9H4v2H1zm4 5h6v4H5z"/></svg>
          <span>555 - 210 - 5006</span>
        </li>
        <li>
          <svg viewBox="0 0 16 14" aria-hidden="true"><path d="M1 2h14v1L8 8 1 3zm0 3 7 5 7-5v7H1z"/></svg>
          <span>tassingfordoralsurgery@mailbox.com</span>
        </li>
        <li>
          <svg viewBox="0 0 16 14" aria-hidden="true"><path d="M1 1h14v9H1zm1.5 1.5v6h11v-6zM6 11h4v1.5h2V14H4v-1.5h2z"/></svg>
          <span>www.tassingfordoralsurgery.com</span>
        </li>
      </ul>
      <p class="address">48 Harwell Road, Tassingford, NY 10999</p>

      <svg class="card-bands" viewBox="0 366 666 32" aria-hidden="true">
        <polygon points="0,366 394,366 436,398 0,398" fill="var(--ink)"/>
        <polygon points="420,376 666,376 666,398 448,398" fill="var(--brand-blue)"/>
      </svg>
    </div>
  </div>
</body>
</html>
```